Core Values poster for our office wall

We have a set of core values in our business and we want to create a nice looking poster to go up on our office wall.

Probably either A1 or A0 sizing.

It is important that the poster represents us as a company and our values.
You can get some ideas on us via the website colours/layout etc - www.lumenfixers.com.au

We need it to communicate our Values and how we love having a fun and encouraging environment.

Values: (which also spell out INSPIRED)
And some sub words related to that one

Initative - Ownership, accountability, innovation
Nurturing - Relationships, Community, Helpful
Success - Empowered
Passion - Fun, Relaxed
Integrity - Trust, Honesty, Respectful, Fortitude
Results - Knowledge, Confidence, Go-getter
Efficiency - Consistent, Organised, Fanatic Discipline
Dependability - Predictability, Security, Responsive, Execution

The below link contains some copies of our logo and also various ones of our company mascot.

https://files.lumenfixers.com.au/share/guest/folder.aspx?id=7d21b3f09a4c6e58d2b7710fa3e92c6d1&key=QmTrWx84pLzNc27yyHKd-Ru&v=3K9TqW
Updates

Sorry everyone, A question made me realise I had left out the sub words to each of the main words. Here is an update. Initative - Ownership, accountability, innovation Nurturing - Relationships, Community, Helpful Success - Empowered Passion - Fun, Relaxed Integrity - Trust, Honesty, Respectful, Fortitude Results - Knowledge, Confidence, Go-getter Efficiency - Consistent, Organised, Fanatic Discipline Dependability - Predictability, Security, Responsive, Execution

Industry/Entity Type

Business

Requirements
Must have
• Good clean clear design
• Represent our company branding

```html
<!DOCTYPE html>
<html lang="en">
<head>
<meta charset="utf-8">
<title>Our Core Values – Lumen Fixers</title>
<link rel="stylesheet" href="https://fonts.googleapis.com/css2?family=Open+Sans:wght@400;600&family=Roboto+Condensed:ital,wght@0,700;1,700&display=swap">
<style>
  :root {
    --sky-top: #e9f7fd;
    --sky-light: #5cc6ef;
    --sky-mid: #15aee6;
    --sky-deep: #0a95d2;
    --band-deep: #1471b5;
    --ink-navy: #1d5e98;
    --ring-navy: #22609f;
    --disc-light: #86d3f3;
    --sub-text: #2b68a6;
    --white: #ffffff;
    --rule: #8aa9c4;
  }
  * { box-sizing: border-box; margin: 0; padding: 0; }
  html, body { width: 851px; height: 1200px; overflow: hidden; }
  body { font-family: "Open Sans", Arial, sans-serif; }

  .poster {
    position: relative;
    width: 851px;
    height: 1200px;
    overflow: hidden;
    background: linear-gradient(180deg,
      var(--sky-light) 0px,
      var(--sky-top) 150px,
      var(--sky-light) 250px,
      var(--sky-mid) 420px,
      var(--sky-mid) 1080px,
      var(--sky-deep) 1200px);
  }

  .sky-haze {
    position: absolute;
    left: 0; top: 60px;
    width: 851px; height: 220px;
  }

  .mascot-silhouette {
    position: absolute;
    left: 20px; top: 265px;
    width: 360px; height: 740px;
    border-radius: 150px 170px 120px 60px;
    background: linear-gradient(180deg, rgba(70,160,215,0.35), rgba(70,160,215,0.18));
  }

  .footer-band {
    position: absolute;
    left: 0; bottom: 0;
    width: 851px; height: 95px;
    background: linear-gradient(180deg, rgba(255,255,255,0.25) 0%, rgba(200,235,250,0.55) 40%, var(--band-deep) 100%);
  }

  .brand {
    position: absolute;
    left: 56px; top: 95px;
    width: 154px; height: 120px;
    border-radius: 46px;
    background: linear-gradient(180deg, #8fd8f5, #4fb3e6);
    display: flex;
    align-items: center;
    justify-content: center;
  }
  .brand-name {
    font-family: "Open Sans", Arial, sans-serif;
    font-weight: 600;
    font-size: 20px;
    line-height: 1.15;
    color: var(--ink-navy);
    text-align: center;
    width: 100px;
  }

  .title {
    position: absolute;
    left: 258px; top: 118px;
    font-family: "Roboto Condensed", "Arial Narrow", sans-serif;
    font-weight: 700;
    font-style: italic;
    font-size: 60px;
    letter-spacing: -0.5px;
    line-height: 1;
    color: var(--ink-navy);
  }
  .title-rule {
    position: absolute;
    left: 248px; top: 197px;
    width: 504px; height: 1.5px;
    background: var(--rule);
  }

  .values { list-style: none; }
  .value {
    position: absolute;
    left: 116px;
    width: 680px;
    height: 94px;
  }
  .value-badge {
    position: absolute;
    left: 0; top: 0;
    width: 94px; height: 94px;
    border-radius: 50%;
    background: var(--ring-navy);
  }
  .value-badge::after {
    content: "";
    position: absolute;
    left: 14px; top: 14px;
    width: 66px; height: 66px;
    border-radius: 50%;
    background: var(--disc-light);
  }
  .value-letter {
    position: absolute;
    left: 0; top: 0;
    width: 94px; height: 94px;
    z-index: 1;
    display: flex; align-items: center; justify-content: center;
    font-family: "Roboto Condensed", "Arial Narrow", sans-serif;
    font-weight: 700;
    font-size: 42px;
    color: var(--white);
  }
  .value-name {
    position: absolute;
    left: 143px; top: 29px;
    font-weight: 600;
    font-size: 18.5px;
    color: var(--white);
    line-height: 1;
  }
  .value-traits {
    position: absolute;
    left: 143px; top: 55px;
    font-weight: 400;
    font-size: 19px;
    color: var(--sub-text);
    line-height: 1;
    white-space: nowrap;
  }
</style>
</head>
<body>
<main class="poster">
  <svg class="sky-haze" viewBox="0 0 851 220" aria-hidden="true">
    <path d="M0 40 C180 10 420 30 620 70 C720 90 800 110 851 130 L851 170 C760 150 640 140 520 150 C360 160 200 150 0 120 Z" fill="#ffffff" opacity="0.45"/>
    <path d="M260 130 C420 120 560 140 680 180 L640 190 C520 160 400 150 260 150 Z" fill="#ffffff" opacity="0.5"/>
  </svg>

  <div class="mascot-silhouette" role="img" aria-label="Faint silhouette of the company mascot behind the values"></div>
  <div class="footer-band" role="img" aria-label="Soft white brushed wave along the bottom edge"></div>

  <div class="brand" role="img" aria-label="Company mascot beside the company name">
    <span class="brand-name">Lumen Fixers</span>
  </div>

  <h1 class="title">OUR CORE VALUES</h1>
  <div class="title-rule"></div>

  <ul class="values">
    <li class="value" style="top:283px">
      <span class="value-badge"></span><span class="value-letter">I</span>
      <span class="value-name">INITIATIVE</span>
      <span class="value-traits">OWNERSHIP - ACCOUNTABILITY - INNOVATION</span>
    </li>
    <li class="value" style="top:384px">
      <span class="value-badge"></span><span class="value-letter">N</span>
      <span class="value-name">NURTURING</span>
      <span class="value-traits">RELATIONSHIPS - COMMUNITY - HELPFUL</span>
    </li>
    <li class="value" style="top:486px">
      <span class="value-badge"></span><span class="value-letter">S</span>
      <span class="value-name">SUCCESS</span>
      <span class="value-traits">EMPOWERMENT</span>
    </li>
    <li class="value" style="top:586px">
      <span class="value-badge"></span><span class="value-letter">P</span>
      <span class="value-name">PASSION</span>
      <span class="value-traits">FUN - RELAXED</span>
    </li>
    <li class="value" style="top:686px">
      <span class="value-badge"></span><span class="value-letter">I</span>
      <span class="value-name">INTEGRITY</span>
      <span class="value-traits">TRUST - HONESTY - RESPECTFUL - FORTITUDE</span>
    </li>
    <li class="value" style="top:786px">
      <span class="value-badge"></span><span class="value-letter">R</span>
      <span class="value-name">RESULTS</span>
      <span class="value-traits">KNOWLEDGE - CONFIDENCE - GO-GETTER</span>
    </li>
    <li class="value" style="top:886px">
      <span class="value-badge"></span><span class="value-letter">E</span>
      <span class="value-name">EFFICIENCY</span>
      <span class="value-traits">CONSISTENT - ORGANISED - FANATIC - DISCIPLINE</span>
    </li>
    <li class="value" style="top:986px">
      <span class="value-badge"></span><span class="value-letter">D</span>
      <span class="value-name">DEPENDABILITY</span>
      <span class="value-traits">PREDICTABILITY - SECURITY - RESPONSIVE - EXECUTION</span>
    </li>
  </ul>
</main>
</body>
</html>
```